Battle of the Bands Flyer

We are looking to have a flyer made for Battle of the Bands event featuring kids. It is a fundraising event hosted by us, BELVIK Contracting. Proceeds raised from the event will benefit Maple and Harbor and Tillman School for Arts. This information should be reflected on the flyer somewhere, and will provide the logos.
We will post a sample of something we mocked up in AI for inspiration.
The title should be "Battle of the Bands".
The subtitle should be "Sky's the Limit"
The date of the event is February 27, 2025 at 5 pm.
The location of the event is Corvin Flight Museum in Irvine, CA.
To register for the event, you can put the contact email as jwelty@belvikcontracting.example.

```html
<!DOCTYPE html>
<html lang="en">
<head>
<meta charset="utf-8">
<title>Battle of the Bands – Sky's the Limit</title>
<link href="https://fonts.googleapis.com/css2?family=Anton&family=Saira+Condensed:wght@600&family=Inter:wght@400&display=swap" rel="stylesheet">
<style>
  :root {
    --mat: #cccccc;
    --ink: #08080c;
    --white: #ffffff;
    --red: #f24a4a;
    --sky: #5f88b8;
    --navy: #1d2d40;
    --tan: #b89870;
    --rust: #8a3d22;
    --orange: #f08a1c;
  }
  * { margin: 0; padding: 0; box-sizing: border-box; }
  html, body { width: 978px; height: 1200px; overflow: hidden; background: var(--mat); }
  .flyer {
    position: absolute; left: 104px; top: 104px; width: 769px; height: 991px;
    background: var(--ink); overflow: hidden;
  }
  .backdrop {
    position: absolute; inset: 0 0 300px 0;
    background:
      radial-gradient(ellipse at 55% 8%, rgba(120,160,205,0.95) 0%, rgba(95,136,184,0.7) 30%, transparent 55%),
      linear-gradient(160deg, var(--navy) 0%, #2c4a66 30%, var(--tan) 55%, var(--rust) 75%, var(--ink) 100%);
  }
  .backdrop::after {
    content: ""; position: absolute; inset: 0;
    background: linear-gradient(180deg, transparent 60%, var(--ink) 100%),
                linear-gradient(90deg, rgba(8,8,12,0.55) 0%, transparent 25%);
  }
  .guitar-art {
    position: absolute; left: 561px; top: 0; width: 208px; height: 775px;
    background: linear-gradient(180deg, #2a2a30 0%, #111116 45%, #050507 70%, #111 100%);
    border-radius: 40px 0 0 120px;
    box-shadow: 0 0 24px rgba(255,255,255,0.35);
  }

  .title-block {
    position: absolute; left: 112px; top: 160px; width: 440px;
    transform: rotate(-8deg); transform-origin: center;
    font-family: "Anton", sans-serif; color: var(--white);
    text-transform: uppercase; font-weight: 400;
  }
  .title-line { display: block; white-space: nowrap; text-align: center; overflow: visible; }
  .title-line > span {
    display: inline-block; transform-origin: center;
    text-shadow:
      -2px 2px 0 var(--ink), -4px 4px 0 var(--ink), -6px 6px 0 var(--ink),
      -8px 8px 0 var(--ink), -10px 10px 0 var(--ink),
      -12px 12px 0 var(--red), 2px -2px 0 var(--red);
  }
  .title-battle, .title-bands { height: 146px; line-height: 146px; font-size: 138px; }
  .title-battle > span, .title-bands > span { transform: scaleY(1.3); }
  .title-ofthe { height: 58px; line-height: 58px; font-size: 48px; text-align: left; padding-left: 58px; }
  .title-ofthe > span { transform: scaleY(1.25); text-shadow: -2px 2px 0 var(--ink), -3px 3px 0 var(--ink); }
  .subtitle { height: 92px; line-height: 92px; font-size: 64px; margin-top: 6px; }
  .subtitle > span {
    transform: scaleY(1.25);
    text-shadow: -2px 2px 0 var(--ink), -4px 4px 0 var(--ink), -6px 6px 0 var(--ink), -7px 7px 0 var(--red), 2px -2px 0 var(--red);
  }

  .info-band {
    position: absolute; left: 91px; width: 454px; background: var(--red);
    color: var(--white); font-family: "Saira Condensed", sans-serif; font-weight: 600;
    text-align: center; white-space: nowrap;
  }
  .event-date { top: 648px; height: 55px; font-size: 42px; line-height: 55px; }
  .event-venue { top: 708px; height: 56px; font-size: 36px; line-height: 56px; }
  .register {
    position: absolute; left: 0; right: 0; top: 808px; text-align: center;
    font-family: "Inter", sans-serif; font-size: 18.5px; color: var(--white); line-height: 27px;
  }
  .register a { color: var(--red); text-decoration: none; }
  .partners {
    position: absolute; left: 0; right: 0; top: 905px; height: 50px;
    display: flex; justify-content: space-around; align-items: center; padding: 0 40px;
  }
  .partner {
    display: flex; align-items: center; gap: 8px;
    font-family: "Saira Condensed", sans-serif; font-weight: 600; font-size: 24px; color: var(--white);
  }
  .partner-mark { width: 14px; height: 14px; background: var(--orange); }
  .partner-mark.round { border-radius: 50%; background: var(--red); }
</style>
</head>
<body>
  <main class="flyer">
    <div class="backdrop" role="img" aria-label="Illustration of a fighter jet flying over a waving American flag"></div>
    <div class="guitar-art" role="img" aria-label="Black electric guitar standing upright"></div>

    <header class="title-block">
      <h1>
        <span class="title-line title-battle"><span>Battle</span></span>
        <span class="title-line title-ofthe"><span>Of the</span></span>
        <span class="title-line title-bands"><span>Bands</span></span>
      </h1>
      <h2 class="title-line subtitle"><span>Sky's the Limit</span></h2>
    </header>

    <p class="info-band event-date">February 27, 2025 at 5 pm.</p>
    <p class="info-band event-venue">Corvin Flight Museum in Irvine, CA</p>

    <p class="register">To register for the event, you can put the contact email as<br>
      <a href="mailto:jwelty@belvikcontracting.example">jwelty@belvikcontracting.example</a></p>

    <footer class="partners">
      <div class="partner"><span class="partner-mark round"></span>Maple and Harbor</div>
      <div class="partner">BELVIK Contracting</div>
      <div class="partner"><span class="partner-mark"></span>Tillman School for Arts</div>
    </footer>
  </main>
</body>
</html>
```